Tide Harbor Finance Business Cards

Looking for a business card for a new mortgage broking business. Name of the business is Tide Harbor Finance. Purpose of the business is to build trust and strong relationships with clients to then assist them with your mortgage lending needs. Most relationships within the business start off as an enquiry, and then can evolve into a 10+ year relationship, servicing clients from purchasing a new home to then upgrading for their family and even then assisting their children with their first home purchase. Business card should communicate financial security and trust.

Target Market(s)

Targeting professional clients who are looking to build a relationship with a knowledgeable mortgage professional

Industry/Entity Type

Finance - Home Loans

Contact Information for Business Card

Peter Colburn, Director, mobile: 0427 903186, email:peter@tideharborfinance.com.au, website: www.tideharborfinance.com.au

Font styles to use
Sans Serif

Requirements
Must have
• On the front: Must have company logo, contact details as above. On the back: slogan, 'Clear choices, calm waters ahead', plus listing services offered: home loans, investment loans, first home buyers, refinancing, car finance

```html
<!DOCTYPE html>
<html lang="en">
<head>
<meta charset="utf-8">
<title>Tide Harbor Finance – Business Cards</title>
<link href="https://fonts.googleapis.com/css2?family=Montserrat:wght@500;600;700&family=Roboto:wght@400;500&display=swap" rel="stylesheet">
<style>
  :root {
    --navy: #014b75;
    --orange: #f0a00a;
    --white: #ffffff;
    --backdrop: #bdbdbd;
    --backdrop-dark: #a3a3a3;
  }
  * { box-sizing: border-box; margin: 0; padding: 0; }
  html, body { width: 1200px; height: 802px; overflow: hidden; }
  body {
    background: linear-gradient(180deg, var(--backdrop) 0%, var(--backdrop-dark) 100%);
    font-family: "Roboto", Arial, sans-serif;
    color: var(--white);
    position: relative;
  }
  .card {
    position: absolute;
    width: 530px;
    height: 300px;
    background: var(--navy);
    border-radius: 22px;
    box-shadow: 0 14px 30px rgba(0,0,0,0.28);
    overflow: hidden;
  }
  .card--front { left: 50px; top: 251px; }
  .card--back  { left: 620px; top: 251px; }

  /* Front */
  .front-wordmark {
    position: absolute; left: 38px; top: 38px;
    font-family: "Montserrat", Arial, sans-serif;
    font-weight: 600; font-size: 31px; line-height: 1.02;
    letter-spacing: 0.5px; text-transform: uppercase;
  }
  .front-mark {
    position: absolute; right: 42px; top: 40px;
    width: 150px; height: 150px;
    border: 9px solid var(--white);
    border-radius: 6px;
  }
  .person { position: absolute; left: 38px; top: 162px; }
  .person__name {
    font-family: "Montserrat", Arial, sans-serif;
    font-weight: 700; font-size: 20px; color: var(--orange);
  }
  .person__role { font-size: 13px; margin-top: 2px; }
  .contacts {
    position: absolute; left: 38px; top: 218px;
    list-style: none; font-size: 13px; line-height: 20px;
  }
  .contacts li { display: flex; align-items: center; gap: 9px; }
  .contacts svg { width: 13px; height: 13px; flex: none; }
  .edge-stripe {
    position: absolute; left: 0; right: 0; bottom: 0; height: 8px;
    background: var(--orange);
  }

  /* Back */
  .back-brand {
    position: absolute; left: 0; right: 0; top: 42px;
    display: flex; justify-content: center; align-items: center; gap: 16px;
  }
  .back-brand__mark {
    width: 74px; height: 74px;
    border: 6px solid var(--white); border-radius: 10px;
  }
  .back-brand__name {
    font-family: "Montserrat", Arial, sans-serif;
    font-weight: 600; font-size: 26px; line-height: 1.02;
    text-transform: uppercase;
  }
  .slogan {
    position: absolute; left: 0; right: 0; top: 150px; text-align: center;
    font-family: "Montserrat", Arial, sans-serif; font-weight: 700; font-size: 22px;
  }
  .services-title {
    position: absolute; left: 0; right: 0; top: 192px; text-align: center;
    font-family: "Montserrat", Arial, sans-serif; font-weight: 700; font-size: 15px;
    letter-spacing: 3.5px; color: var(--orange);
  }
  .services {
    position: absolute; left: 30px; right: 30px; top: 218px;
    display: flex; flex-wrap: wrap; justify-content: center; gap: 2px 16px;
    list-style: none; font-size: 15px; line-height: 22px;
  }
  .services li::before { content: "• "; }
</style>
</head>
<body>
  <section class="card card--front" aria-label="Business card front">
    <div class="front-wordmark">Tide<br>Harbor<br>Finance</div>
    <div class="front-mark" aria-hidden="true"></div>
    <div class="person">
      <div class="person__name">Peter Colburn</div>
      <div class="person__role">Director</div>
    </div>
    <ul class="contacts">
      <li>
        <svg viewBox="0 0 14 14" aria-hidden="true"><rect x="3.5" y="1" width="7" height="12" rx="1.5" fill="none" stroke="#f0a00a" stroke-width="1.6"/><circle cx="7" cy="11" r="0.8" fill="#f0a00a"/></svg>
        0427 903186
      </li>
      <li>
        <svg viewBox="0 0 14 14" aria-hidden="true"><rect x="1" y="3" width="12" height="8" fill="#f0a00a"/><path d="M1 3 L7 8 L13 3" fill="none" stroke="#014b75" stroke-width="1.2"/></svg>
        peter@tideharborfinance.com.au
      </li>
      <li>
        <svg viewBox="0 0 14 14" aria-hidden="true"><circle cx="7" cy="7" r="6" fill="#f0a00a"/><path d="M1 7 H13 M7 1 C4 4 4 10 7 13 M7 1 C10 4 10 10 7 13" fill="none" stroke="#014b75" stroke-width="1"/></svg>
        www.tideharborfinance.com.au
      </li>
    </ul>
    <div class="edge-stripe"></div>
  </section>

  <section class="card card--back" aria-label="Business card back">
    <div class="back-brand">
      <div class="back-brand__mark" aria-hidden="true"></div>
      <div class="back-brand__name">Tide<br>Harbor<br>Finance</div>
    </div>
    <p class="slogan">Clear choices, calm waters ahead</p>
    <h2 class="services-title">LISTING SERVICES OFFERED</h2>
    <ul class="services">
      <li>Home loans</li>
      <li>Investment loans</li>
      <li>First home buyers</li>
      <li>Refinancing</li>
      <li>Car finance</li>
    </ul>
  </section>
</body>
</html>
```